Reed & Vale NC grand opening (for BILLBOARD)

Advertising the grand opening of our cannabis/hemp shop in NC. We will sell all things hemp (flower, cartridges, disposables, edibles, creams, lotions, pet products etc...)

Requirements
Must have
• include, open starting Aug 1, but grand opening Aug 15th.
Nice to have
• Difference slogan ideas "Save some cash, buy our grass" "Find your perfect high at Reed & Vale cannabis store" "Experience Nature's Gift: Reed & Vale Cannabis Store"

```html
<!DOCTYPE html>
<html lang="en">
<head>
<meta charset="utf-8">
<title>Reed &amp; Vale Grand Opening Billboard</title>
<link rel="stylesheet" href="https://fonts.googleapis.com/css2?family=Jost:wght@400;500;600&family=Montserrat:wght@800&family=Oswald:wght@500&display=swap">
<style>
  :root {
    --backdrop: #dedcdc;
    --paper: #ffffff;
    --leaf-green: #80bf44;
    --forest-green: #136a3f;
    --navy: #0f1234;
    --ink: #1b1b1b;
    --headline-ink: #0d1420;
    --chalk: #f3f1ea;
  }
  * { margin: 0; padding: 0; box-sizing: border-box; }
  html, body {
    width: 1200px;
    height: 1200px;
    overflow: hidden;
    background: var(--backdrop);
  }
  .billboard {
    position: absolute;
    left: 77px;
    top: 339px;
    width: 1045px;
    height: 523px;
    background: var(--paper);
    overflow: hidden;
  }
  .billboard-shapes {
    position: absolute;
    inset: 0;
    width: 1045px;
    height: 523px;
  }
  .brand {
    position: absolute;
    left: 56px;
    top: 88px;
    display: flex;
    align-items: center;
    gap: 14px;
  }
  .brand-dot {
    width: 26px;
    height: 26px;
    border-radius: 50%;
    background: var(--leaf-green);
  }
  .brand-name {
    font-family: 'Jost', sans-serif;
    font-weight: 500;
    font-size: 62px;
    line-height: 1;
    color: var(--leaf-green);
    letter-spacing: -0.5px;
  }
  .slogan {
    position: absolute;
    left: 54px;
    top: 190px;
    font-family: 'Jost', sans-serif;
    font-weight: 400;
    font-size: 29px;
    line-height: 38px;
    color: var(--ink);
    white-space: nowrap;
  }
  .product-panel {
    position: absolute;
    left: 0;
    top: 329px;
    width: 493px;
    height: 161px;
    background: var(--navy);
    padding: 16px 0 0 54px;
    color: var(--paper);
    font-family: 'Jost', sans-serif;
    white-space: nowrap;
  }
  .product-title {
    font-weight: 600;
    font-size: 27px;
    line-height: 34px;
  }
  .product-list {
    list-style: none;
    font-weight: 400;
    font-size: 23px;
    line-height: 30px;
  }
  .open-date {
    position: absolute;
    right: 63px;
    top: 42px;
    text-align: right;
    font-family: 'Montserrat', sans-serif;
    font-weight: 800;
    font-size: 36px;
    line-height: 44px;
    color: var(--headline-ink);
    white-space: nowrap;
  }
  .grand-opening {
    position: absolute;
    left: 535px;
    top: 258px;
    width: 440px;
    text-align: center;
    font-family: 'Oswald', sans-serif;
    font-weight: 500;
    font-size: 66px;
    line-height: 88px;
    letter-spacing: 1px;
    color: var(--chalk);
    white-space: nowrap;
  }
  .grand-opening span { display: block; }
</style>
</head>
<body>
  <main class="billboard">
    <svg class="billboard-shapes" viewBox="0 0 1045 523" aria-hidden="true">
      <defs>
        <linearGradient id="panel-sheen" x1="0" y1="0" x2="1" y2="0">
          <stop offset="0" stop-color="#ffffff" stop-opacity="0.14"/>
          <stop offset="1" stop-color="#ffffff" stop-opacity="0"/>
        </linearGradient>
      </defs>
      <polygon class="corner-band" points="429,0 1045,0 1045,259" fill="var(--leaf-green)"/>
      <polygon class="accent-strip" points="603,96 1045,276 966,523 450,523" fill="var(--leaf-green)"/>
      <polygon class="date-panel" points="616,96 1045,270 966,523 463,523" fill="var(--forest-green)"/>
      <polygon class="panel-sheen" points="648,128 800,190 710,523 530,523" fill="url(#panel-sheen)"/>
      <polygon class="panel-sheen" points="805,192 900,231 845,523 730,523" fill="url(#panel-sheen)"/>
    </svg>

    <div class="brand">
      <span class="brand-name">Reed &amp; Vale</span>
      <span class="brand-dot"></span>
    </div>

    <p class="slogan">Find your perfect high at<br>Reed &amp; Vale cannabis store</p>

    <section class="product-panel">
      <h2 class="product-title">We will sell all things hemp</h2>
      <ul class="product-list">
        <li>• Flower • Cartridges</li>
        <li>• Disposables • Edibles</li>
        <li>• Creams • otions • pet products etc...)</li>
      </ul>
    </section>

    <p class="open-date">Open starting<br>Aug 1st</p>

    <h1 class="grand-opening"><span>Aug 15th</span><span>Grand Opening</span></h1>
  </main>
</body>
</html>
```